KORBALT

The business want a professional looking business card. We have a scetch we will add but want the extra upgrade, and would like more suggestions for variations of our business cards.

```html
<!DOCTYPE html>
<html lang="en">
<head>
<meta charset="utf-8">
<title>KORBALT business card</title>
<link href="https://fonts.googleapis.com/css2?family=Montserrat:wght@400;500;700&display=swap" rel="stylesheet">
<style>
  :root {
    --backdrop: #ece8e3;
    --card-white: #f7f5f1;
    --gold: #c9962e;
    --gold-deep: #b07c1c;
    --gold-light: #e9b553;
    --charcoal: #2b2b2b;
    --ink: #2f2f2f;
    --white: #ffffff;
  }
  * { box-sizing: border-box; margin: 0; padding: 0; }
  html, body { width: 1200px; height: 800px; overflow: hidden; }
  body {
    background: var(--backdrop);
    font-family: "Montserrat", sans-serif;
    display: flex;
    align-items: center;
    justify-content: center;
    gap: 40px;
  }
  .card {
    position: relative;
    width: 540px;
    height: 310px;
    border-radius: 18px;
    overflow: hidden;
    box-shadow: 0 10px 28px rgba(0,0,0,0.12);
  }
  .card-front { background: var(--card-white); }
  .card-back {
    background: linear-gradient(135deg, var(--gold-light), var(--gold) 70%, var(--gold-deep));
    display: flex;
    align-items: center;
    justify-content: center;
  }
  .waves { position: absolute; inset: 0; width: 100%; height: 100%; }
  .brand-block {
    position: absolute;
    left: 30px;
    top: 92px;
    width: 170px;
    text-align: center;
  }
  .brand-name {
    font-weight: 700;
    font-size: 30px;
    letter-spacing: 3px;
    color: var(--gold);
  }
  .brand-since {
    display: flex;
    align-items: center;
    gap: 6px;
    margin-top: 6px;
    font-size: 10px;
    letter-spacing: 2.5px;
    color: var(--ink);
  }
  .brand-since::before, .brand-since::after {
    content: ""; flex: 1; height: 1px; background: var(--gold);
  }
  .divider {
    position: absolute;
    left: 222px;
    top: 70px;
    width: 1px;
    height: 150px;
    background: var(--gold);
  }
  .contact-block {
    position: absolute;
    left: 246px;
    top: 64px;
    color: var(--ink);
  }
  .holder-heading {
    font-weight: 700;
    font-size: 15px;
    letter-spacing: 0.5px;
    color: var(--gold-deep);
  }
  .holder-role, .holder-name { font-size: 13px; line-height: 1.35; }
  .holder-role { margin-top: 6px; }
  .contact-list { list-style: none; margin-top: 14px; }
  .contact-list li {
    display: flex; align-items: center; gap: 9px;
    font-size: 11px; line-height: 1; margin-bottom: 9px;
  }
  .contact-list svg { width: 11px; height: 11px; fill: var(--gold-deep); flex: none; }
  .back-name {
    font-weight: 700;
    font-size: 46px;
    letter-spacing: 6px;
    color: var(--white);
  }
</style>
</head>
<body>
  <section class="card card-front">
    <svg class="waves" viewBox="0 0 540 310" preserveAspectRatio="none" aria-hidden="true">
      <path d="M0 228 Q130 214 270 252 Q140 236 0 252Z" fill="var(--charcoal)"/>
      <path d="M0 258 Q160 240 300 272 Q440 292 540 230 L540 310 L0 310Z" fill="var(--gold)"/>
      <path d="M250 266 Q430 268 540 168" fill="none" stroke="var(--gold-deep)" stroke-width="5"/>
      <path d="M300 282 Q460 270 540 196" fill="none" stroke="var(--gold-light)" stroke-width="4"/>
    </svg>
    <div class="brand-block">
      <div class="brand-name">KORBALT</div>
      <div class="brand-since">SINCE 2026</div>
    </div>
    <div class="divider"></div>
    <div class="contact-block">
      <h1 class="holder-heading">KORBALT L SOLBAKKEN</h1>
      <p class="holder-role">CEO &amp; Founder</p>
      <p class="holder-name">Lars Henrik Solbakken</p>
      <ul class="contact-list">
        <li><svg viewBox="0 0 24 24"><path d="M6.6 10.8a15 15 0 006.6 6.6l2.2-2.2a1 1 0 011-.25 11.4 11.4 0 003.6.57 1 1 0 011 1V20a1 1 0 01-1 1A17 17 0 013 4a1 1 0 011-1h3.5a1 1 0 011 1c0 1.25.2 2.45.57 3.57a1 1 0 01-.25 1z"/></svg>004791234567</li>
        <li><svg viewBox="0 0 24 24"><path d="M2 5h20v14H2z M2 5l10 8 10-8" fill="none" stroke="var(--gold-deep)" stroke-width="2"/></svg>korbalt.llc@mailbox.com</li>
        <li><svg viewBox="0 0 24 24"><circle cx="12" cy="12" r="9.5" fill="none" stroke="var(--gold-deep)" stroke-width="2"/><path d="M2.5 12h19M12 2.5c-4 4.5-4 14.5 0 19M12 2.5c4 4.5 4 14.5 0 19" fill="none" stroke="var(--gold-deep)" stroke-width="1.6"/></svg>www.korbalt.llc</li>
      </ul>
    </div>
  </section>
  <section class="card card-back">
    <div class="back-name">KORBALT</div>
  </section>
</body>
</html>
```